Item Change Management Brochure / FAQ

Create a very stunning, infographic based brochure around a process Birch Supply Company calls "Item Change Management". The audience for the brochure are Birch Supply retail store owners and operators who need to be amazed by the program. This brochure is to make it easy for Birch Supply store owners to understand the program, its benefits, and the process behind it. Here are some important notes about the brochure:

* Must all fit content on 2 pages - a front and back side - 8-1/2x11"
* Font must be no smaller than size 11 Calibri. Calibri does NOT have to be used but just want to level set the size.
* Use Birch Supply colors (red, black, and white).
* Graphics and design must be super amazing to look at
* The document Word titled "Item Change Management" has most of the content needed. Use the provided photos as you see fit.
* Important: I would like the Excel file to appear in the 2-page brochure. The Word document titled Item Change Management Sales Floor and Back Office Actions is the legend for the Excel file (rows 8,9,16, and 17 of Excel file).

Target Market(s)

Birch Supply store owners and operators

Industry/Entity Type

Retail

Font styles to use
Sans Serif

Colors
EB3D1F
EC4F4E
F09395
F8D3D4
FCEDEE

Requirements
Must have
• * Unique and look extremely creative, 8-1/2x11", font size that is readable to average eye, Birch Supply colors, all content provided (images provided are optional), infographics where possible, the chart must look incredible.
Should not have
• Boring, too standard, traditional.

```html
<!DOCTYPE html>
<html lang="en">
<head>
<meta charset="utf-8">
<title>Item Change Management – FAQ</title>
<link href="https://fonts.googleapis.com/css2?family=Open+Sans:wdth,wght@75..100,300..800&family=PT+Sans+Narrow:wght@400;700&display=swap" rel="stylesheet">
<style>
  :root{
    --red:#e31b37;
    --ink:#231f20;
    --black:#1e1c1d;
    --white:#ffffff;
    --grey-row:#ececec;
    --grey-line:#cfcfcf;
    --text:#333333;
    --art-a:#f8d3d4;
    --art-b:#d8ecf7;
  }
  *{box-sizing:border-box;margin:0;padding:0}
  html,body{width:783px;height:1200px;overflow:hidden;background:var(--white)}
  body{font-family:"Open Sans",Arial,sans-serif;color:var(--text);position:relative}

  .page{position:relative;width:783px;height:1200px;overflow:hidden}

  /* Header */
  .masthead{position:absolute;left:0;top:0;width:783px;height:215px}
  .masthead-shape{position:absolute;inset:0}
  .brand{position:absolute;left:40px;top:50px;display:flex;align-items:center;gap:10px}
  .brand-name{font-weight:800;font-size:19px;color:var(--red);letter-spacing:.5px;text-transform:uppercase}
  .brand-divider{width:1px;height:28px;background:#777}
  .brand-unit{font-weight:700;font-size:14px;line-height:14px;color:var(--white);letter-spacing:.3px}
  .brand-unit span{display:block;color:var(--red);font-size:16px;line-height:16px}
  .doc-title{position:absolute;left:38px;top:100px;line-height:1}
  .doc-title .line1{display:block;font-weight:300;font-size:33px;color:var(--white);letter-spacing:.5px}
  .doc-title .line2{display:block;font-weight:800;font-size:47px;color:var(--red);letter-spacing:.3px;margin-top:4px}
  .faq-art{position:absolute;left:528px;top:38px;width:222px;height:165px;border-radius:50% 46% 40% 48%;
    background:radial-gradient(circle at 55% 40%,var(--art-b) 0%,var(--art-a) 55%,rgba(255,255,255,0) 75%)}
  .faq-art-word{position:absolute;left:0;right:0;top:40px;text-align:center;font-weight:800;font-size:78px;color:var(--red);letter-spacing:-2px;line-height:1}

  /* Section heading */
  .section-head{position:absolute;left:0;right:0;top:236px;text-align:center}
  .section-head h2{font-size:21px;font-weight:700;color:var(--ink);letter-spacing:.2px}
  .section-head h2 em{font-style:normal;color:var(--red)}
  .section-rule{position:relative;width:420px;height:1px;background:var(--grey-line);margin:8px auto 0}
  .section-rule::after{content:"";position:absolute;left:50%;top:-2px;width:48px;height:5px;margin-left:-24px;border-radius:3px;background:var(--red)}

  /* FAQ columns */
  .faq-columns{position:absolute;top:292px;left:38px;right:22px;display:flex;gap:28px;height:600px}
  .faq-col{flex:1;display:flex;flex-direction:column;justify-content:space-between}
  .faq-col.right{justify-content:flex-start;gap:16px}
  .faq-item{position:relative;padding-left:46px}
  .faq-num{position:absolute;left:0;top:0;width:34px;height:34px;border-radius:50%;
    border:3px solid var(--red);background:var(--black);color:var(--white);
    font-size:12px;font-weight:700;display:flex;align-items:center;justify-content:center;
    box-shadow:0 0 0 2px var(--white) inset}
  .faq-item::before{content:"";position:absolute;left:16px;top:38px;bottom:2px;border-left:1px dotted #888}
  .faq-item.last::before{display:none}
  .faq-q{font-size:10.5px;font-weight:600;font-stretch:80%;color:var(--ink);line-height:13.5px;margin-top:2px;white-space:nowrap}
  .faq-q em{font-style:normal;color:var(--red)}
  .faq-a{font-family:"PT Sans Narrow",sans-serif;font-size:11.5px;line-height:14.5px;color:var(--text);margin-top:6px}

  /* Data table */
  .copy-table{position:absolute;left:42px;right:28px;top:912px}
  .copy-table-head{position:relative;height:38px;border-radius:12px 12px 0 0;background:var(--red);
    display:flex;align-items:center;padding-left:58px;color:var(--white);font-size:12.5px;font-weight:600;font-stretch:90%;white-space:nowrap}
  .copy-table-head .faq-num{left:12px;top:2px;background:var(--white);color:var(--ink);border-color:var(--black)}
  .copy-grid{display:grid;grid-template-columns:144px 143px 137px 143px 1fr;border-radius:0 0 10px 10px;overflow:hidden}
  .copy-cell{position:relative;height:24px;display:flex;align-items:center;padding-left:10px;font-size:9.5px;color:#444;white-space:nowrap;overflow:hidden;border-right:1px solid var(--grey-line)}
  .copy-cell:nth-child(5n){border-right:none}
  .copy-cell.tick{padding-left:24px}
  .row-shade{background:var(--grey-row)}
  .copy-cell.tick::before{content:"";position:absolute;left:9px;top:8px;width:9px;height:9px;border:1px solid #777;background:var(--white)}
  .copy-cell.tick::after{content:"";position:absolute;left:12.5px;top:8px;width:3px;height:6px;border:solid #444;border-width:0 1.2px 1.2px 0;transform:rotate(40deg)}

  /* Footer */
  .footer{position:absolute;left:0;bottom:0;width:783px;height:90px}
  .footer-shape{position:absolute;inset:0}
  .footer-contact{position:absolute;left:45px;top:30px;font-size:19px;font-weight:700;color:var(--white);white-space:nowrap}
  .footer-contact span{color:var(--red);margin-right:8px}
  .footer-email{position:absolute;left:462px;top:30px;display:flex;align-items:center;gap:8px;font-size:15.5px;font-weight:600;color:var(--ink);white-space:nowrap}
</style>
</head>
<body>
<div class="page">

  <header class="masthead">
    <svg class="masthead-shape" width="783" height="215" viewBox="0 0 783 215" aria-hidden="true">
      <polygon points="0,0 484,0 395,215 0,215" fill="#1e1c1d"/>
      <polygon points="400,215 433,124 476,215" fill="#e31b37"/>
    </svg>
    <div class="brand">
      <span class="brand-name">Birch Supply</span>
      <span class="brand-divider"></span>
      <span class="brand-unit">STORE SYSTEMS &amp;<span>OPERATIONS</span></span>
    </div>
    <h1 class="doc-title">
      <span class="line1">ITEM CHANGE</span>
      <span class="line2">MANAGEMENT</span>
    </h1>
    <div class="faq-art" role="img" aria-label="Illustration of people with laptops and plants arranged around large red FAQ letters">
      <div class="faq-art-word">FAQ</div>
    </div>
  </header>

  <div class="section-head">
    <h2>FREQUENTLY ASKED <em>QUESTIONS</em></h2>
    <div class="section-rule"></div>
  </div>

  <main class="faq-columns">
    <section class="faq-col left">
      <article class="faq-item">
        <div class="faq-num">01</div>
        <p class="faq-q">Why do I even need to do Item Change<br><em>Management (ICM)?</em></p>
        <p class="faq-a">ICM simplifies and reduces the amount time and effort to manage the process of identifying and taking action against canceled, replacement, and reinstated items. Without ICM, the process of doing so is manual and laborious, error prone, and ultimately can result in taking lost sales. Contrarily, leveraging ICM (versus other manual approaches) typically saves stores between 8-12 hours per month, increase inventory accurateness, and improves operational effectiveness on the sales floor.</p>
      </article>
      <article class="faq-item">
        <div class="faq-num">02</div>
        <p class="faq-q">How frequently should <em>I be working ICM?</em></p>
        <p class="faq-a">Weekly. This keeps the execution manageable and steady. Aim for consistency by performing ICM the same day each week.</p>
      </article>
      <article class="faq-item">
        <div class="faq-num">03</div>
        <p class="faq-q">My computer is ordering the replacement SKU when I’m<br><em>not out of stock on the discontinued product. Why?</em></p>
        <p class="faq-a">Confirm option configuration setting 9972 is set to option ‘2’. Doing so tells the system to order the new product only when the discontinued item falls to zero on hand.</p>
      </article>
      <article class="faq-item">
        <div class="faq-num">04</div>
        <p class="faq-q">I heard ICM merges product information. I’ve been<br><em>using RCIN in Falcon for years to do that. Do I still need<br>to use RCIN?</em></p>
        <p class="faq-a">Managing items via ICM renders the need to do RCIN obsolete. ICM doesn’t technically ‘merge’ items because doing so creates inventory issues as well as a loss of visibility to discontinued SKUs. ICM, on the other hand, copies over certain key information from the discontinued item to the new item, keeping the discontinued item intact to retain visibility and minimize long-term inventory accuracy issues.</p>
      </article>
      <article class="faq-item last">
        <div class="faq-num">05</div>
        <p class="faq-q">I’m in on ICM. <em>How do I get started?</em></p>
        <p class="faq-a">Great! Start by reviewing the Birch Way of Retailing Practice titled Item Change Management (Cancelled, Replacement, Temporary Closeout, and Reinstated Items) – Setup. Path: BIRCHNET &gt; About Birch – Birch Way of Retailing &gt; BWOR Search: ICM.</p>
      </article>
    </section>

    <section class="faq-col right">
      <article class="faq-item">
        <div class="faq-num">06</div>
        <p class="faq-q">What in the world is the RICR report, and how does<br><em>it relate to ICM?</em></p>
        <p class="faq-a">RICR stands for ‘Item Change Report’ and prints after finalizing your work in ICM. Review it in the back office and on the sales floor as a means to update location codes and bin labels.</p>
      </article>
      <article class="faq-item">
        <div class="faq-num">07</div>
        <p class="faq-q">Does ICM have any effect on my in-stock<br><em>percentage measurement?</em></p>
        <p class="faq-a">Undoubtably. Stores regularly leveraging ICM weekly have shown to have a higher in-stock percentage than those that don’t. ICM allows retailers to react faster and more effectively to items going away ensuring an effective plan is in place. Also, taking action against temporary out of stocks using ICM doesn’t negatively impact your in-stock percentage.</p>
      </article>
      <article class="faq-item">
        <div class="faq-num">08</div>
        <p class="faq-q">If I don’t stock the SKU, <em>will it appear in ICM?</em></p>
        <p class="faq-a">No. Your ICM list is store specific, not a report of everything carried in the RSC. In other words, items you have not sold or purchased from the RSC in the last three years do not appear in the program for you to action.</p>
      </article>
      <article class="faq-item">
        <div class="faq-num">09</div>
        <p class="faq-q">I have five stores in my chain. Can I review and execute ICM<br><em>for all of them in one fell swoop?</em></p>
        <p class="faq-a">Sure. The reporting in ICM can be reviewed and executed centrally creating greater efficiencies when executing. Upon entering the BIRCHNET application, simply click the multi-store icon to select the stores you want to work on.</p>
      </article>
      <article class="faq-item">
        <div class="faq-num">10</div>
        <p class="faq-q">I don’t know if my SKUs are updating properly<br><em>How do I confirm?</em></p>
        <p class="faq-a">Compare the BIRCHNET PDF (available upon finalizing your work) to the Falcon RICR report to ensure all information has transmitted properly. If need be, you can also run the RICR report manually to serve as an audit tool. Within the ICM application, there is also an option to review previously finalized items for further investigation.</p>
      </article>
      <article class="faq-item last">
        <div class="faq-num">11</div>
        <p class="faq-q">Who do I contact with any further <em>questions and support?</em></p>
        <p class="faq-a">Your field representative is always available to help answer questions. For further details about the program, you can also contact the Store Systems and Operations team.</p>
      </article>
    </section>
  </main>

  <section class="copy-table">
    <div class="copy-table-head">
      <div class="faq-num">12</div>
      When I replace an item with another, what information is exactly ‘copied’ over to the replacement SKU?
    </div>
    <div class="copy-grid">
      <div class="copy-cell tick row-shade">Date Added</div>
      <div class="copy-cell tick row-shade">Sales History</div>
      <div class="copy-cell tick row-shade">PO Season Code</div>
      <div class="copy-cell tick row-shade">Tally</div>
      <div class="copy-cell tick row-shade">Discountable</div>

      <div class="copy-cell tick">ROP Protect</div>
      <div class="copy-cell tick">Max Stock Level</div>
      <div class="copy-cell tick">Tax Status</div>
      <div class="copy-cell tick">Loading Required</div>
      <div class="copy-cell tick">User codes</div>

      <div class="copy-cell tick row-shade">Order Point</div>
      <div class="copy-cell tick row-shade">Special Fees</div>
      <div class="copy-cell tick row-shade"># of Labels</div>
      <div class="copy-cell tick row-shade">Birch MSU's</div>
      <div class="copy-cell tick row-shade">Promo History</div>

      <div class="copy-cell tick">Location code(s)</div>
      <div class="copy-cell tick">Signature Required</div>
      <div class="copy-cell tick">Expanded Sales History</div>
      <div class="copy-cell tick">CPP Discounts</div>
      <div class="copy-cell tick">Sells with SKU</div>

      <div class="copy-cell tick row-shade">ExpandedPromo History</div>
      <div class="copy-cell tick row-shade">Popularity Code</div>
      <div class="copy-cell row-shade"></div>
      <div class="copy-cell row-shade"></div>
      <div class="copy-cell row-shade"></div>
    </div>
  </section>

  <footer class="footer">
    <svg class="footer-shape" width="783" height="90" viewBox="0 0 783 90" aria-hidden="true">
      <polygon points="0,0 400,0 470,90 0,90" fill="#1e1c1d"/>
      <polygon points="448,62 783,62 783,72 456,72" fill="#e31b37"/>
      <polygon points="456,72 783,72 783,90 470,90" fill="#1e1c1d"/>
    </svg>
    <p class="footer-contact"><span>CONTACT INFORMATION:</span>555.014.2290</p>
    <p class="footer-email">
      <svg width="15" height="11" viewBox="0 0 16 12" aria-hidden="true">
        <rect x="0" y="0" width="16" height="12" fill="#e31b37"/>
        <polyline points="0,0 8,7 16,0" fill="none" stroke="#fff" stroke-width="1.4"/>
      </svg>
      storeoperations@birchsupply.com
    </p>
  </footer>

</div>
</body>
</html>
```